Walk Boldly into Morning: 48 Days to a Year of Courage and Calm

This is a non-fiction, self-help book. The first edition was published a decade ago, and it needs a new design. Nothing too literal (no actual hearts on the cover) but something inspirational or perhaps something quite plain. The current cover is below for reference, but I DO NOT want something similar to that. It is outdated.

The cover must include:

1. Title: Walk Boldly into Morning
2. Subtitle: 48 Days to a Year of Courage and Calm
3. Author Name: Dean Forsythe

It should also have plenty of "white space" in other words the fonts shouldnt be so big that they take up the whole cover.

Dimensions: 9" x 6.25"

Target Market(s)

adults interested in personal development

Font styles to use
Serif
Script

Colors

Designer to choose colors to be used in the design.

Requirements
Must have
• Classic look and feel. The current design is too busy. I have included examples of the style I like below. I'm open to a singular graphic/photo but nothing more than that. Probably plain text is best.
• Please look at the samples I have included of best-selling books in the genre that I like. The cover should be modeled after these.

```html
<!DOCTYPE html>
<html lang="en">
<head>
<meta charset="utf-8">
<title>Walk Boldly into Morning — Dean Forsythe</title>
<link rel="stylesheet" href="https://fonts.googleapis.com/css2?family=Cormorant+Garamond:wght@400;500;600&family=Pinyon+Script&display=swap">
<style>
  :root {
    --paper: #ffffff;
    --sea-deep: #12a6dc;
    --sea-mid: #33c1ec;
    --sea-light: #74dcf6;
    --ink-grey: #8f8f8f;
  }
  html, body {
    margin: 0;
    padding: 0;
    overflow: hidden;
    background: var(--paper);
  }
  .cover {
    position: relative;
    width: 840px;
    height: 1200px;
    background: var(--paper);
    overflow: hidden;
  }
  .title {
    position: absolute;
    top: 250px;
    left: 0;
    width: 100%;
    margin: 0;
    display: flex;
    flex-direction: column;
    align-items: center;
    text-align: center;
    font-weight: 600;
  }
  .title-word {
    display: block;
    font-family: "Cormorant Garamond", serif;
    font-size: 88px;
    line-height: 100px;
    letter-spacing: 0.14em;
    padding-left: 0.14em;
    text-transform: uppercase;
    background: linear-gradient(100deg, var(--sea-deep) 0%, var(--sea-mid) 50%, var(--sea-light) 100%);
    -webkit-background-clip: text;
    background-clip: text;
    color: transparent;
  }
  .title-joiner {
    display: block;
    font-family: "Pinyon Script", cursive;
    font-weight: 400;
    font-size: 68px;
    line-height: 84px;
    color: var(--sea-mid);
  }
  .subtitle {
    position: absolute;
    top: 842px;
    left: 0;
    width: 100%;
    margin: 0;
    text-align: center;
    font-family: "Cormorant Garamond", serif;
    font-weight: 500;
    font-size: 22px;
    letter-spacing: 0.14em;
    text-transform: uppercase;
    color: var(--ink-grey);
  }
  .author {
    position: absolute;
    top: 1070px;
    left: 0;
    width: 100%;
    margin: 0;
    text-align: center;
    font-family: "Cormorant Garamond", serif;
    font-weight: 400;
    font-size: 42px;
    letter-spacing: 0.22em;
    padding-left: 0.22em;
    box-sizing: border-box;
    text-transform: uppercase;
    color: var(--ink-grey);
  }
</style>
</head>
<body>
  <main class="cover">
    <h1 class="title" aria-label="Walk Boldly into Morning">
      <span class="title-word">Walk</span>
      <span class="title-word">Boldly</span>
      <span class="title-joiner">into</span>
      <span class="title-word">Morning</span>
    </h1>
    <p class="subtitle">48 Days to a Year of Courage and Calm</p>
    <p class="author">Dean Forsythe</p>
  </main>
</body>
</html>
```